Brightleaf Practice Partners, Inc (www.brightleafpracticepartnrs.example) would like to design a website to convey a level of professionalism to healthcare providers that we are the place form them to visit for Contin. Education, Marketing and Management, Joint Venture Partnerships, etc.
We think we would like a WP Site so that we can use the dynamic and static sides of it's capabilities. We also want to have something that acts as a membership side where members can post their Bio and CV's and prospective employers can post help wanted ads.

Target Market(s)

Pediatricians, Pediatric Dentist, Employers seeking these doctors

Industry/Entity Type

Healthcare

Requirements
Must have
• Services:
Resumes/Bio
Help Wanted
Continuing Education Programs
Marketing & Management

```html
<!DOCTYPE html>
<html lang="en">
<head>
<meta charset="utf-8">
<title>Brightleaf Practice Partners</title>
<link rel="stylesheet" href="https://fonts.googleapis.com/css2?family=Arimo:wght@400&family=Questrial&family=Yanone+Kaffeesatz:wght@300;400&family=Dancing+Script:wght@500&display=swap">
<style>
:root{
  --page:#e8e8e6;
  --teal:#2f7b99;
  --teal-dark:#24617c;
  --footer:#245f79;
  --heading:#2f86ad;
  --orange:#d9661f;
  --text:#2a2a2a;
  --body:#3b3b3b;
  --rule:#5a6066;
  --field:#dde3d3;
  --field-border:#8d918b;
  --navy:#13305a;
}
*{box-sizing:border-box;margin:0;padding:0}
html,body{width:934px;height:1200px;overflow:hidden;background:var(--page)}
body{position:relative;font-family:Arimo,Arial,sans-serif;color:var(--body)}
.abs{position:absolute}

.site-header{left:7px;top:3px;width:919px;height:61px;background:linear-gradient(180deg,#3b88a6,var(--teal) 60%,var(--teal-dark))}
.brand{left:25px;top:7px;font-family:"Yanone Kaffeesatz",sans-serif;font-weight:400;font-size:24px;color:#fff;letter-spacing:.2px}
.tagline{left:27px;top:37px;font-family:"Dancing Script",cursive;font-size:15px;color:#e6eef2}
.main-nav{right:14px;top:18px;display:flex;gap:22px;font-family:"Yanone Kaffeesatz",sans-serif;font-size:17px;font-variant:small-caps;color:#fff;letter-spacing:.4px}
.main-nav span.current{border-bottom:1px solid #cfe2ea;padding-bottom:1px}

.rule-title{left:26px;width:882px;height:14px}
.rule-title svg{position:absolute;left:0;top:0}
.section-title{top:109px;left:0;width:934px;text-align:center;font-family:"Yanone Kaffeesatz",sans-serif;font-weight:300;font-size:30px;color:#1f3c58}
.section-title span{background:var(--page);padding:0 10px}
.intro{left:60px;top:148px;width:818px;font-size:13px;line-height:20px;color:var(--text)}

.login-row{left:0;top:227px;width:934px;text-align:center;font-family:"Yanone Kaffeesatz",sans-serif;font-size:19px}
.login-row span.wrap{background:var(--page);padding:0 4px}
.login-doctor{color:var(--teal)}
.login-employer{color:var(--orange)}
.dot{display:inline-block;width:13px;height:13px;border-radius:50%;background:#2a2f33;margin:0 10px;vertical-align:-1px}

.feature-photo{width:240px;height:240px;border-radius:50%;top:290px;border:3px solid}
.photo-doctor{left:46px;border-color:#3f7c96;background:radial-gradient(circle at 45% 40%,#f3efe9,#d9c9bd 55%,#c9d2d8)}
.photo-team{left:347px;border-color:#8a4a1c;background:radial-gradient(circle at 50% 45%,#e8d5bd,#a98565 55%,#5c6b80)}
.photo-social{left:650px;border-color:#2d2d2d;background:radial-gradient(circle at 55% 50%,#fdfdfd,#cfcfcf 50%,#8a8a8a)}

.feature{width:248px;top:560px}
.feature h2{font-weight:400;font-size:19px;color:var(--heading);text-align:center;margin-bottom:12px}
.feature p{font-size:11.5px;line-height:14.7px;text-align:justify;margin-bottom:14.7px}
.f1{left:46px}.f2{left:342px}.f3{left:641px}

.contact-title{left:39px;top:806px;font-family:Questrial,sans-serif;font-size:22px;color:#1f5577;letter-spacing:1px}
.label{top:851px;font-size:15px;color:var(--text)}
.field{top:875px;height:33px;background:var(--field);border:2px solid var(--field-border);border-radius:7px}
.select-arrow{position:absolute;right:1px;top:1px;width:36px;height:27px;border-radius:6px;background:linear-gradient(#c9ccc6,#a9aca6)}
.send{left:786px;top:874px;width:121px;height:34px;border:2px solid var(--field-border);border-radius:8px;background:var(--field);font-family:Arimo,Arial,sans-serif;font-size:21px;color:var(--heading);text-align:center;line-height:29px}
.divider{left:44px;top:934px;width:854px;height:1px;background:var(--rule)}

.service{top:970px;width:252px}
.service h3{font-family:Questrial,sans-serif;font-weight:400;font-size:19px;color:var(--heading);margin-bottom:13px}
.service p{font-size:11.5px;line-height:14.7px;text-align:justify}
.service .more{float:right;color:var(--orange);font-size:10.5px}
.s1{left:36px}.s2{left:344px}.s3{left:651px}

.site-footer{left:30px;top:1099px;width:879px;height:96px;background:linear-gradient(180deg,#2a6a86,var(--footer))}
.footer-links{left:16px;font-size:10.5px;color:#eef4f7}
.footer-links.l1{top:30px;word-spacing:3px}
.footer-links.l2{top:57px}
.social{width:33px;height:33px;border-radius:5px;background:var(--navy);border:1px solid #0a1c36}
.stetho{left:784px;top:-12px;width:90px;height:100px;border-radius:45%;background:radial-gradient(circle,#cfd6da,#6f8893 55%,transparent 72%)}
</style>
</head>
<body>

<header class="site-header abs">
  <div class="brand abs">Brightleaf Practice Partners</div>
  <div class="tagline abs">The profiles of pediatricians</div>
  <nav class="main-nav abs">
    <span class="current">Home</span><span>About</span><span>Upload Your CV</span><span>Employeers Add</span><span>My Account</span>
  </nav>
</header>

<svg class="abs" style="left:0;top:0" width="934" height="1200" aria-hidden="true">
  <g fill="none" stroke="#3c4247" stroke-width="1">
    <line x1="39" y1="125" x2="895" y2="125"/>
    <circle cx="33" cy="125" r="6" fill="#e8e8e6" stroke-width="1.3"/>
    <circle cx="902" cy="125" r="6" fill="#e8e8e6" stroke-width="1.3"/>
    <line x1="41" y1="239" x2="896" y2="239"/>
    <circle cx="35" cy="239" r="6" fill="#e8e8e6" stroke-width="1.3"/>
    <circle cx="902" cy="239" r="6" fill="#e8e8e6" stroke-width="1.3"/>
    <line x1="206" y1="821" x2="897" y2="821"/>
    <circle cx="903" cy="821" r="6" fill="#e8e8e6" stroke-width="1.3"/>
  </g>
</svg>

<h1 class="section-title abs"><span>Brightleaf Practice Partners</span></h1>
<p class="intro abs">Lorem ipsum dolor sit amet, consectetur adipisicing elit, sed do eiusmod tempor incididunt ut labore et dolore magna aliqua. Ut enim ad minim veniam, quis nostrud exercitation ullamco laboris nisi ut aliquip ex ea commodo consequat. Duis aute irure dolor in reprehenderit in voluptate velit esse cillum dolore eu fugiat nulla pariatur. Excepteur sint occaecat cupidatat non proident, sunt in culpa qui officia deserunt mollit anim id est.</p>

<div class="login-row abs"><span class="wrap"><span class="login-doctor">Doctor's Login</span><span class="dot"></span><span class="login-employer">Employeers Login</span></span></div>

<div class="feature-photo photo-doctor abs" role="img" aria-label="Photo of a pediatrician examining a baby"></div>
<div class="feature-photo photo-team abs" role="img" aria-label="Photo of a smiling team of healthcare professionals"></div>
<div class="feature-photo photo-social abs" role="img" aria-label="Illustration of grey globe-shaped social media icons"></div>

<section class="feature f1 abs">
  <h2>Doctors' Profiles</h2>
  <p>Lorem ipsum dolor sit amet, consectetur adipiscing elit. Etiam bibendum lacinia mauris, in ornare augue tempus vel. Fusce sed nisi libero, sed euismod quam. Donec ut tincidunt lacus. Cras pretium ullamcorper urna, vel lobortis nisl tempor eu. Phasellus fringilla eleifend arcu id sodales.</p>
  <p>Lorem ipsum dolor sit amet, consectetur adipiscing elit. Etiam bibendum lacinia mauris, in ornare augue tempus vel. Fusce sed nisi libero, sed euismod quam. Donec ut tincidunt lacus. Cras</p>
</section>
<section class="feature f2 abs">
  <h2>Employeers' Details</h2>
  <p>Lorem ipsum dolor sit amet, consectetur adipiscing elit. Etiam bibendum lacinia mauris, in ornare augue tempus vel. Fusce sed nisi libero, sed euismod quam. Donec ut tincidunt lacus. Cras pretium ullamcorper urna, vel lobortis nisl tempor eu. Phasellus fringilla eleifend arcu id sodales.</p>
  <p>Lorem ipsum dolor sit amet, consectetur adipiscing elit. Etiam bibendum lacinia mauris, in ornare augue tempus vel. Fusce sed nisi libero, sed euismod quam. Donec ut tincidunt lacus. Cras</p>
</section>
<section class="feature f3 abs">
  <h2>Wanted Adds</h2>
  <p>Lorem ipsum dolor sit amet, consectetur adipiscing elit. Etiam bibendum lacinia mauris, in ornare augue tempus vel. Fusce sed nisi libero, sed euismod quam. Donec ut tincidunt lacus. Cras pretium ullamcorper urna, vel lobortis nisl tempor eu. Phasellus fringilla eleifend arcu id sodales.</p>
  <p>Lorem ipsum dolor sit amet, consectetur adipiscing elit. Etiam bibendum lacinia mauris, in ornare augue tempus vel. Fusce sed nisi libero, sed euismod quam. Donec ut tincidunt lacus. Cras</p>
</section>

<h2 class="contact-title abs">CONTACT ME</h2>
<div class="label abs" style="left:39px">Name:</div>
<div class="label abs" style="left:278px">Email:</div>
<div class="label abs" style="left:531px">Specialist</div>
<div class="field abs" style="left:35px;width:223px"></div>
<div class="field abs" style="left:274px;width:233px"></div>
<div class="field abs" style="left:530px;width:241px">
  <div class="select-arrow"><svg width="36" height="27" aria-hidden="true"><polyline points="11,11 18,17 25,11" fill="none" stroke="#f2f2f2" stroke-width="3" stroke-linecap="round" stroke-linejoin="round"/></svg></div>
</div>
<div class="send abs">send</div>
<div class="divider abs"></div>

<section class="service s1 abs">
  <h3>Continuing Education</h3>
  <p>Lorem ipsum dolor sit amet, consectetur adipiscing elit. Etiam bibendum lacinia mauris, in ornare augue tempus vel. Fusce sed nisi libero, sed euismod quam. Donec ut tincidunt lacus. <span class="more">Know more</span></p>
</section>
<section class="service s2 abs">
  <h3>Managment</h3>
  <p>Lorem ipsum dolor sit amet, consectetur adipiscing elit. Etiam bibendum lacinia mauris, in ornare augue tempus vel. Fusce sed nisi libero, sed euismod quam. Donec ut tincidunt lacus. <span class="more">Know more</span></p>
</section>
<section class="service s3 abs">
  <h3>Marketing</h3>
  <p>Lorem ipsum dolor sit amet, consectetur adipiscing elit. Etiam bibendum lacinia mauris, in ornare augue tempus vel. Fusce sed nisi libero, sed euismod quam. Donec ut tincidunt lacus. <span class="more">Know more</span></p>
</section>

<footer class="site-footer abs">
  <div class="footer-links l1 abs">Home About Upload Your CV Employeers Add My Account</div>
  <div class="footer-links l2 abs">Copyright Statement &nbsp;|&nbsp; Privacy Policy &nbsp;|&nbsp; Terms &amp; Conditions</div>
  <div class="social abs" style="left:664px;top:12px" role="img" aria-label="Social link"></div>
  <div class="social abs" style="left:703px;top:12px" role="img" aria-label="Social link"></div>
  <div class="social abs" style="left:664px;top:50px" role="img" aria-label="Social link"></div>
  <div class="social abs" style="left:703px;top:50px" role="img" aria-label="Email">
    <svg width="31" height="31" aria-hidden="true"><rect x="5" y="9" width="21" height="14" rx="1.5" fill="#e9eef3"/><polyline points="5,9 15.5,17 26,9" fill="none" stroke="#13305a" stroke-width="1.5"/></svg>
  </div>
  <div class="stetho abs" role="img" aria-label="Illustration of a stethoscope"></div>
</footer>

</body>
</html>
```